BRWK branding
Stationery & misc. Design Elements
Thank Delphine!
To all designers: My client has chosen Orvo Design as the winner on this project. Thanks to all for the hard work and revised designs. Keep an eye out for another project for Birchwood Spinal Care Logo. Thanks for the efforts.
Delphine
@ Brambly : I think some of your winning designs(concept) are similar....
So,are these copied from others???
No,Dear Friend,Everything is separate from others as like as me.
Don't be upset... :)
Wishing you all the best.
-A Friend,
OrvoDesigner
http://www.draftvane.example/drafts/display/contest/10001/draft/300001
http://www.draftvane.example/drafts/display/contest/10002/draft/300002
http://www.draftvane.example/drafts/display/contest/10003/draft/300003
http://www.draftvane.example/drafts/display/contest/10004/draft/300004
http://www.draftvane.example/drafts/display/contest/10005/draft/300005
http://www.draftvane.example/drafts/display/contest/10006/draft/300006
http://www.draftvane.example/drafts/display/contest/10007/draft/300007
@ Dear Brambly : Yes,I already won that contest. I think - you guess something similar like that. Would you compare again ,please? It is not copied from that.Please,See carefully Envelope and the Letterhead again(that you thinking).
Only the color format are similar that I like most.Without this everything is different(about the color code,Color area,address position,watermark,line and the logo position).Is it clear,dear?
Thanks for your hard trying about the design.
I really wish your success.
(A Competitor and a friend.)
-OrvoDesigner
Orvo Design,
u already winning this design
To all designers: remember to submit a page or so of additional design elements for use in future marketing collateral - as stated in
the project brief. Thanks
Correction ** New logo uploaded 11/15
Please upload ai or eps of your logo.

```html
<!DOCTYPE html>
<html lang="en">
<head>
<meta charset="utf-8">
<title>Birchwood Spinal Care – Stationery</title>
<link href="https://fonts.googleapis.com/css2?family=Cinzel:wght@400;600&display=swap" rel="stylesheet">
<style>
  :root {
    --brand-blue: #1f6db3;
    --brand-blue-dark: #155792;
    --brand-blue-light: #4aa0dc;
    --paper: #ffffff;
    --board: #ffffff;
    --frame: #d9d9d9;
    --ink-soft: #3b7fbf;
  }
  html, body {
    margin: 0;
    padding: 0;
    width: 1200px;
    height: 676px;
    overflow: hidden;
    background: var(--board);
  }
  .board {
    position: relative;
    width: 1200px;
    height: 676px;
    font-family: "Cinzel", serif;
  }
  .board-frame {
    position: absolute;
    left: 34px; top: 24px;
    width: 1134px; height: 618px;
    border: 2px solid var(--frame);
    box-sizing: border-box;
  }
  .sheet {
    position: absolute;
    background: var(--paper);
    box-shadow: 0 3px 8px rgba(0,0,0,0.28), 0 0 1px rgba(0,0,0,0.25);
  }
  .top-band {
    position: absolute;
    left: 0; right: 0; top: 0;
    height: 12px;
    background: linear-gradient(to bottom, var(--brand-blue-light), var(--brand-blue-dark));
  }
  .brand {
    position: absolute;
    display: flex;
    align-items: center;
    gap: 8px;
    color: var(--brand-blue);
    font-weight: 600;
    white-space: nowrap;
  }
  .brand-dot {
    border-radius: 50%;
    background: var(--brand-blue);
    flex: none;
  }
  .address {
    position: absolute;
    color: var(--ink-soft);
    font-size: 7px;
    letter-spacing: 0.3px;
    white-space: nowrap;
  }

  /* Envelope front */
  .envelope-front { left: 65px; top: 161px; width: 492px; height: 218px; }
  .envelope-front .brand { left: 14px; top: 44px; font-size: 17px; }
  .envelope-front .brand-dot { width: 14px; height: 14px; }
  .envelope-front .address { left: 14px; top: 106px; }

  /* Envelope back */
  .envelope-back { left: 65px; top: 410px; width: 492px; height: 226px; }
  .envelope-flap { position: absolute; left: 0; top: 0; width: 492px; height: 84px; }

  /* Letterhead */
  .letterhead { left: 612px; top: 48px; width: 343px; height: 571px; }
  .letterhead .top-band { height: 10px; }
  .letterhead .brand { left: 48px; top: 90px; font-size: 15px; }
  .letterhead .brand-dot { width: 12px; height: 12px; }
  .letterhead .address { left: 48px; top: 124px; font-size: 6px; }

  /* Business card */
  .business-card { left: 960px; top: 182px; width: 139px; height: 108px; }
  .business-card .top-band { height: 5px; }
  .business-card .brand { right: 8px; top: 16px; font-size: 8px; gap: 4px; }
  .business-card .brand-dot { width: 7px; height: 7px; }
  .card-person {
    position: absolute; left: 8px; top: 52px;
    color: var(--brand-blue); font-size: 5.5px; font-weight: 600; line-height: 1.4;
  }
  .card-person .role { font-weight: 400; color: var(--ink-soft); }
  .business-card .address { left: 8px; top: 80px; font-size: 4px; }
</style>
</head>
<body>
<main class="board">
  <div class="board-frame"></div>

  <section class="sheet envelope-front" aria-label="Envelope front">
    <div class="top-band"></div>
    <div class="brand"><span class="brand-dot"></span>Birchwood Spinal Care</div>
    <p class="address">412 Alder Crest Avenue, Fenwick, NJ 07990</p>
  </section>

  <section class="sheet envelope-back" aria-label="Envelope back">
    <svg class="envelope-flap" viewBox="0 0 492 84" preserveAspectRatio="none">
      <defs>
        <linearGradient id="flapGradient" x1="0" y1="0" x2="1" y2="0">
          <stop offset="0" stop-color="#1d63a6"/>
          <stop offset="0.5" stop-color="#4aa0dc"/>
          <stop offset="1" stop-color="#1d63a6"/>
        </linearGradient>
      </defs>
      <path d="M0 0 H492 V34 Q480 70 400 76 Q246 86 92 76 Q12 70 0 34 Z" fill="url(#flapGradient)"/>
    </svg>
  </section>

  <section class="sheet letterhead" aria-label="Letterhead">
    <div class="top-band"></div>
    <div class="brand"><span class="brand-dot"></span>Birchwood Spinal Care</div>
    <p class="address">412 Alder Crest Avenue, Fenwick, NJ 07990</p>
  </section>

  <section class="sheet business-card" aria-label="Business card">
    <div class="top-band"></div>
    <div class="brand"><span class="brand-dot"></span>Birchwood Spinal Care</div>
    <div class="card-person">
      Lena Marsh, M.D.<br>
      <span class="role">Spine Surgeon</span>
    </div>
    <p class="address">Tel 555 0142 | info@birchwood.example</p>
  </section>
</main>
</body>
</html>
```